Disability and mental health support work company requires business card

Specialising
Wrenfield Disability is a new QCAP service aimed toward QCAP participants with a history of criminal justice, psychosocial/mental health, intellectual, and cognitive disabilities.

Our focus
Focusing on providing core QCAP supports for community participation, daily activities and supported independent living.

Authentic
Likeminded people wanting to make a difference in participant's lives.

Our aim to provide holistic and empowering supports targeted towards creating independence and guidance for all participants and families.
Over 35 years of experience working with people that have psychosocial, intellectual, and cognitive disabilities.

Industry/Entity Type

disability and mental health

Contact Information for Business Card

logo - business name

Colors
0054AA
0677BA
7BADD7
CADEEF
E8F1F8
FFF300
FFF600
FEFA6F
FFFEC7
FFFEE8

Requirements
Must have
• want double sided business cards(wont let me change it)
Should not have
• any disability related pictures

```html
<!DOCTYPE html>
<html lang="en">
<head>
<meta charset="utf-8">
<title>Wrenfield Disability – Business Card</title>
<link rel="stylesheet" href="https://fonts.googleapis.com/css2?family=Arimo:wght@400;700&display=swap">
<style>
  :root {
    --backdrop: #2b2b2b;
    --card: #0b0b0b;
    --badge: #163a63;
    --badge-rim: #7badd7;
    --accent: #7badd7;
    --text: #ffffff;
    --rule: #5a5a5a;
  }
  * { box-sizing: border-box; margin: 0; padding: 0; }
  html, body { width: 1200px; height: 900px; overflow: hidden; }
  body {
    background: var(--backdrop);
    font-family: "Arimo", Arial, sans-serif;
    position: relative;
  }
  .card {
    position: absolute;
    left: 280px;
    width: 640px;
    height: 366px;
    background: var(--card);
    box-shadow: 0 10px 30px rgba(0,0,0,.5);
  }
  .card--front { top: 70px; }
  .card--back { top: 470px; }

  .brand-badge {
    position: absolute;
    width: 240px;
    height: 240px;
    border-radius: 50%;
    background: var(--badge);
    border: 3px solid var(--badge-rim);
    display: flex;
    align-items: center;
    justify-content: center;
    text-align: center;
  }
  .card--front .brand-badge { left: 44px; top: 63px; }
  .card--back .brand-badge { left: 200px; top: 63px; }
  .brand-name {
    color: var(--accent);
    font-weight: 700;
    font-size: 24px;
    line-height: 1.2;
    text-transform: uppercase;
    letter-spacing: 1px;
  }

  .divider {
    position: absolute;
    left: 318px;
    top: 70px;
    width: 1px;
    height: 226px;
    background: var(--rule);
  }
  .details {
    position: absolute;
    left: 340px;
    top: 78px;
    color: var(--text);
  }
  .person-name {
    color: var(--accent);
    font-weight: 700;
    font-size: 22px;
    letter-spacing: .5px;
    text-transform: uppercase;
  }
  .person-role { font-size: 15px; margin-top: 2px; }
  .contact-list { list-style: none; margin-top: 16px; }
  .contact-item {
    display: flex;
    align-items: center;
    gap: 10px;
    font-size: 15px;
    height: 26px;
  }
  .contact-icon { width: 20px; height: 20px; flex: none; }
  .address { font-size: 15px; line-height: 1.35; margin-top: 14px; padding-left: 30px; }
</style>
</head>
<body>
  <section class="card card--front">
    <div class="brand-badge"><span class="brand-name">Wrenfield<br>Disability</span></div>
    <div class="divider"></div>
    <div class="details">
      <h1 class="person-name">Marcus Hale</h1>
      <p class="person-role">Managing Director</p>
      <ul class="contact-list">
        <li class="contact-item">
          <svg class="contact-icon" viewBox="0 0 20 20"><circle cx="10" cy="10" r="10" fill="#7badd7"/><path d="M6.5 5.5l2 0 1 2.5-1.3 1a6 6 0 0 0 2.8 2.8l1-1.3 2.5 1v2a1 1 0 0 1-1 1A8.5 8.5 0 0 1 5.5 6.5a1 1 0 0 1 1-1z" fill="#0b0b0b"/></svg>
          07-3555 0142
        </li>
        <li class="contact-item">
          <svg class="contact-icon" viewBox="0 0 20 20"><circle cx="10" cy="10" r="10" fill="#7badd7"/><rect x="6.5" y="4.5" width="7" height="11" rx="1" fill="none" stroke="#0b0b0b" stroke-width="1.4"/><circle cx="10" cy="13.5" r=".8" fill="#0b0b0b"/></svg>
          0412-555 087
        </li>
        <li class="contact-item">
          <svg class="contact-icon" viewBox="0 0 20 20"><circle cx="10" cy="10" r="10" fill="#7badd7"/><rect x="5" y="6.5" width="10" height="7" fill="none" stroke="#0b0b0b" stroke-width="1.3"/><path d="M5 6.5l5 4 5-4" fill="none" stroke="#0b0b0b" stroke-width="1.3"/></svg>
          info@wrenfieldcare.com
        </li>
        <li class="contact-item">
          <svg class="contact-icon" viewBox="0 0 20 20"><circle cx="10" cy="10" r="10" fill="#7badd7"/><g fill="none" stroke="#0b0b0b" stroke-width="1.1"><circle cx="10" cy="10" r="5.5"/><ellipse cx="10" cy="10" rx="2.3" ry="5.5"/><path d="M4.5 10h11M5.3 7.3h9.4M5.3 12.7h9.4"/></g></svg>
          www.wrenfieldcare.com
        </li>
      </ul>
      <p class="address">18 Carrow Street, Milton<br>4064, Queensland</p>
    </div>
  </section>

  <section class="card card--back">
    <div class="brand-badge"><span class="brand-name">Wrenfield<br>Disability</span></div>
  </section>
</body>
</html>
```